Morrow Electrics needs a flyer design

A flyer that outlines what my business offers
-Switchboard upgrades
-Pump and bore installations
-House Re-wires
-Safety switches and smoke alarms
-TV points and aerials
-Powerpoints
-Security systems and lights
-LED lighting
-Renovations/extensions
-Phone and data points
-Ceiling fans
-Audio and visual
-Under ground consumer mains

Add some specials i am offering:
-LED down lights supplied and installed for just $59ea
-Electrical property reports for just $100
(free with rectified work completed)
-Safety switches supplied and installed $150ea

Target Market(s)

Domestic and commercial customers

Industry/Entity Type

Business

Font styles to use
Sans Serif

Colors
ffffff
9bcb3c

Requirements
Must have
• i was unable to load pictures for the specials. So a picture next to each item on special.
• Include these details:
• Registered contracting number: EC58307
• ABN: 64218503927
• Mobile: 0417682943
• Email: liam@morrowelectrics.example
• 12 month guarantee on workmanship

```html
<!DOCTYPE html>
<html lang="en">
<head>
<meta charset="utf-8">
<title>Morrow Electrics Flyer</title>
<link href="https://fonts.googleapis.com/css2?family=Exo+2:wght@500;600;700&family=Mulish:wght@400;700&display=swap" rel="stylesheet">
<style>
:root{
  --green:#3aaa48;
  --green-soft:#e2efdd;
  --grey-dark:#58595b;
  --text:#444;
  --white:#fff;
  --bg:#2d2d2d;
}
*{box-sizing:border-box;margin:0;padding:0}
html,body{width:1200px;height:1200px;overflow:hidden;background:var(--bg)}
body{font-family:"Mulish",sans-serif;color:var(--text)}
.flyer{position:absolute;left:136px;top:0;width:927px;height:1200px;background:var(--white);overflow:hidden}
.header-tagline{position:absolute;left:55px;top:74px;font-family:"Exo 2",sans-serif;font-weight:600;font-size:27px;color:var(--green);letter-spacing:.3px}
.header-details{position:absolute;left:55px;top:108px;font-size:16px;line-height:22px;color:#555;letter-spacing:.3px}
.brand{position:absolute;left:602px;top:56px;display:flex;align-items:center;gap:12px}
.brand-square{width:107px;height:107px;background:var(--green)}
.brand-name{font-family:"Exo 2",sans-serif;font-weight:600;font-size:29px;line-height:33px;color:var(--green);letter-spacing:1.5px;text-transform:uppercase}
.hero-photo{position:absolute;left:0;top:180px;width:927px;height:343px;
  background:linear-gradient(100deg,#c9541f 0%,#e2a12a 22%,#3a3a3a 45%,#b63a2a 65%,#e8b59c 85%,#c2735a 100%)}
.intro{position:absolute;left:55px;top:541px;width:818px;font-size:16.5px;line-height:22px;text-align:justify;color:#555}
.intro b{color:#333}
.services{position:absolute;left:55px;top:630px;width:850px;display:grid;grid-template-columns:285px 285px 280px}
.services ul{list-style:none}
.services li{display:flex;align-items:flex-start;gap:12px;font-size:16.5px;line-height:21px;color:#555;margin-bottom:14px}
.services svg{flex:none;width:26px;height:26px;stroke:var(--green);fill:none;stroke-width:1.8}
.specials-band{position:absolute;left:0;top:877px;width:927px;height:323px;background:var(--green-soft)}
.special{position:absolute;top:828px;width:290px;text-align:center}
.special-badge{width:98px;height:98px;border-radius:50%;border:2px solid var(--green);background:var(--white);margin:0 auto 14px;display:flex;align-items:center;justify-content:center;overflow:hidden}
.badge-photo{width:88px;height:88px;border-radius:50%}
.special-title{font-family:"Exo 2",sans-serif;font-weight:600;font-size:25px;line-height:27px;color:var(--green)}
.special-text{font-size:17px;line-height:24px;color:#333}
.special-price{font-family:"Exo 2",sans-serif;font-weight:600;font-size:25px;color:var(--green)}
.special-note{font-size:12px;color:#333}
.divider{position:absolute;top:897px;width:3px;height:167px;background:linear-gradient(#fff0,#b8c4b6,#fff0)}
.footer-art{position:absolute;left:0;top:1020px;width:927px;height:180px}
.contact{position:absolute;left:55px;top:1100px;color:var(--white);font-size:21px;line-height:28px}
.contact div{display:flex;align-items:center;gap:9px}
.contact svg{width:19px;height:19px;stroke:var(--white);fill:none;stroke-width:1.6}
.phone{position:absolute;right:55px;top:1108px;display:flex;align-items:center;gap:10px;color:var(--white);font-family:"Mulish",sans-serif;font-weight:700;font-size:38px}
.phone svg{width:30px;height:30px;stroke:var(--white);fill:none;stroke-width:1.8}
</style>
</head>
<body>
<main class="flyer">
  <p class="header-tagline">12 month guarantee on workmanship</p>
  <p class="header-details">Registered contracting number: EC58307<br>ABN: 64218503927</p>
  <div class="brand">
    <div class="brand-square"></div>
    <div class="brand-name">Morrow<br>Electrics</div>
  </div>

  <div class="hero-photo" role="img" aria-label="Photo of an electrician testing a switchboard with a yellow multimeter"></div>

  <p class="intro">We <b>service and repair</b> our residential customers with excellence. We do sales, service and installation and make sure our customers feel good at home or business. We also provide estimates on new installations. The most important thing is the quality and attention to detail that we provide.</p>

  <section class="services">
    <ul>
      <li><svg viewBox="0 0 26 26"><rect x="2" y="6" width="22" height="14"/><rect x="6" y="9" width="5" height="8"/><rect x="15" y="9" width="5" height="8"/></svg>Switchboard upgrades</li>
      <li><svg viewBox="0 0 26 26"><rect x="9" y="8" width="15" height="13"/><path d="M2 12h7M4 6v15M12 11h9M12 15h9M12 18h9"/></svg>Pump and bore<br>installations</li>
      <li><svg viewBox="0 0 26 26"><path d="M3 23 14 12M14 12l6-8M14 12l7 1M11 9l4 6"/></svg>House Re-wires</li>
      <li><svg viewBox="0 0 26 26"><ellipse cx="13" cy="9" rx="11" ry="4"/><path d="M4 11l3 5h12l3-5M9 19v4M13 19v4M17 19v4"/></svg>Safety switches and<br>smoke alarms</li>
    </ul>
    <ul>
      <li><svg viewBox="0 0 26 26"><path d="M4 24l6-10 6 6-12 4zM10 14l8-8M16 4a6 6 0 0 1 6 6M17 1a9 9 0 0 1 8 8"/></svg>TV points and aerials</li>
      <li><svg viewBox="0 0 26 26"><rect x="2" y="5" width="22" height="16"/><path d="M7 9v8M10 9v8M16 11h2M16 15h2"/></svg>Powerpoints</li>
      <li><svg viewBox="0 0 26 26"><rect x="2" y="5" width="22" height="16"/><rect x="5" y="8" width="6" height="10"/><path d="M14 9h2M18 9h2M14 13h2M18 13h2M14 17h2M18 17h2"/></svg>Security systems<br>and lights</li>
      <li><svg viewBox="0 0 26 26"><path d="M4 22 14 4l8 14zM4 22l5 2"/></svg>LED lighting</li>
      <li><svg viewBox="0 0 26 26"><path d="M3 23 15 11M13 5l8 8M17 3l6 6M3 3l20 20M5 9l4-4"/></svg>Renovations/extensions</li>
    </ul>
    <ul>
      <li><svg viewBox="0 0 26 26"><circle cx="9" cy="15" r="6"/><path d="M13 11l9-8M17 10l5-4M3 15h-1"/></svg>Phone and data points</li>
      <li><svg viewBox="0 0 26 26"><path d="M13 4v9M2 11l11 2 11-2M13 13l-3 10M13 13l3 10"/></svg>Ceiling fans</li>
      <li><svg viewBox="0 0 26 26"><path d="M2 9h5l7-6v20l-7-6H2zM18 9a5 5 0 0 1 0 8M21 6a9 9 0 0 1 0 14"/></svg>Audio and visual</li>
      <li><svg viewBox="0 0 26 26"><circle cx="13" cy="13" r="10"/><path d="M1 13h24"/></svg>Under ground<br>consumer mains</li>
    </ul>
  </section>

  <div class="specials-band"></div>
  <div class="divider" style="left:310px"></div>
  <div class="divider" style="left:612px"></div>

  <article class="special" style="left:8px">
    <div class="special-badge"><div class="badge-photo" role="img" aria-label="Photo of an LED down light fitting" style="background:radial-gradient(circle,#f6f6e0 0%,#cfcfcf 45%,#8a8a8a 100%)"></div></div>
    <h2 class="special-title">LED down lights</h2>
    <p class="special-text">supplied and<br>installed for just</p>
    <p class="special-price">$59ea</p>
  </article>

  <article class="special" style="left:317px">
    <div class="special-badge">
      <svg width="60" height="70" viewBox="0 0 60 70"><path d="M18 2v16M42 2v16" stroke="#111" stroke-width="7" stroke-linecap="round"/><path d="M6 18h48v14c0 14-10 22-24 22S6 46 6 32z" fill="#111"/><rect x="24" y="52" width="12" height="16" fill="#111"/><path d="M33 22 23 37h8l-4 11 11-16h-8z" fill="#fff"/></svg>
    </div>
    <h2 class="special-title">Electrical<br>property reports</h2>
    <p class="special-text">for just</p>
    <p class="special-price">$100</p>
    <p class="special-note">(free with rectified work completed)</p>
  </article>

  <article class="special" style="left:626px">
    <div class="special-badge"><div class="badge-photo" role="img" aria-label="Photo of a switchboard with safety switches" style="background:linear-gradient(180deg,#9b9b9b,#e9e9e9 40%,#bdbdbd 70%,#6f6f6f)"></div></div>
    <h2 class="special-title">Safety switches</h2>
    <p class="special-text">supplied and installed</p>
    <p class="special-price">$150ea</p>
  </article>

  <svg class="footer-art" viewBox="0 0 927 180" preserveAspectRatio="none">
    <polygon points="0,19 927,156 927,180 0,180" fill="var(--grey-dark)"/>
    <polygon points="927,11 129,180 927,180" fill="var(--green)"/>
  </svg>

  <div class="contact">
    <div><svg viewBox="0 0 20 20"><circle cx="10" cy="10" r="8"/><path d="M7 7l6 3-3 1-1 3z"/></svg>www.morrowelectrics.example</div>
    <div><svg viewBox="0 0 20 20"><circle cx="10" cy="10" r="8"/><rect x="6" y="7" width="8" height="6"/><path d="M6 7l4 3 4-3"/></svg>liam@morrowelectrics.example</div>
  </div>
  <div class="phone"><svg viewBox="0 0 30 30"><circle cx="15" cy="15" r="13"/><path d="M10 8l3 0 1 4-2 1c1 2 3 4 5 5l1-2 4 1v3c-7 1-13-5-12-12z"/></svg>0417-682-943</div>
</main>
</body>
</html>
```